Web Design Project

My website was fine - years ago. But it's way, way overdue for an overhaul. When I started my business almost 20 years ago, I wanted to be edgy. And my website was just that. Color, style, voice. Edgy. Today, my clients are corporations. I'm older, more experienced - but still a little edgy. It's controlled edge. What I want now is sophisticated. Savvy. Corporate but cool. Grown up.

My clients are primarily - but not exclusively - in healthcare. But I don't want a healthcare site. I provide the following services:
1. Writing - white papers, brochures, web pages, speechwriting, etc.
2. Marketing strategy
3. Public relations services
4. Thought leader development
5. Training
I couldn't upload all the icons but I can send them. They correspond with the pages as follows and should be used in the design:

1. Writing- nib.png
2. Marketing strategy-compass.png
3. Public relations services-microphone.png
4. Thought leader development-lightbulb.png
5. Training: cogs-training.png or key.png

I will have a blog, and a portfolio of some kind.

I don't want something that looks like a template.
Updates

Reason: Just made this a committed payment. I apologize for not doing so from the start. Nobody should work for free.

Reason: Several folks have asked to resubmit, and it has taken me a while to provide feedback.

Dear Designers,

I am so sorry to have been so slow to select. I've had professional and personal issues to deal with. I am actively trying to select a design, however, and will do so in the next two days. Thanks so much for your patience and hard work.

Rhoda

Thanks so much to everyone who has submitted a design. I had great luck crowdsourcing my logo, but I'm starting to realize that website design is a totally different animal. All of your designs are great, but they all look exactly like templates. And maybe that's the way it's supposed to be, the way it should be. I don't want to use stock photography. It needs to be more personalized than that. I'm open to illustration or even using my own photo on the site, but stock photography won't work for me. If anyone wants to submit something else - and I understand if you don't - please feel free. 

Target Market(s)

C-suite executives; corporations, larger businesses who need marketing writing

Industry/Entity Type

Healthcare

Requirements
Must have
• Logo (somewhere)
Icons
Nice to have
• Level-specific page design (e.g, Home = Level 1, Tabs = Level 2, etc). I'd like it to have a certain order.

```html
<!DOCTYPE html>
<html lang="en">
<head>
<meta charset="utf-8">
<title>The Vantage Communications</title>
<link href="https://fonts.googleapis.com/css2?family=Ubuntu:ital,wght@0,400;0,500;0,700;1,400&display=swap" rel="stylesheet">
<style>
:root{
  --orange:#f0a000;
  --orange-band:#f39314;
  --orange-text:#f07d00;
  --purple:#6a2c91;
  --purple-light:#7e3dab;
  --purple-dark:#5a2180;
  --ink:#333;
  --body:#555;
  --muted:#888;
  --footer:#5b5b5b;
  --white:#fff;
}
*{box-sizing:border-box;margin:0;padding:0}
html,body{width:1077px;height:1200px;overflow:hidden;background:var(--white)}
body{font-family:"Ubuntu",sans-serif;color:var(--body)}
.stage{position:relative;width:1200px;height:1337px;transform:scale(.8975);transform-origin:0 0;background:var(--white)}
.top-band{position:absolute;left:0;top:0;width:1200px;height:212px;background:var(--orange)}
.page{position:absolute;left:120px;top:27px;width:960px;height:1134px;background:linear-gradient(#f7f7f7,#fff 120px);box-shadow:0 0 6px rgba(0,0,0,.15)}
.abs{position:absolute}

.brand{left:132px;top:43px}
.brand-mark{position:absolute;left:61px;top:0;width:42px;height:42px;background:var(--orange);border-radius:3px}
.brand-name{position:absolute;left:0;top:54px;white-space:nowrap;font-size:30px;font-weight:400;letter-spacing:1px;color:var(--purple)}

.contact{right:174px;top:66px;text-align:right;font-size:18px;color:var(--body);line-height:31px}
.contact strong{color:var(--purple);font-weight:500}
.contact .mail{color:var(--orange-text);font-size:14px}

.nav{left:130px;top:149px;width:940px;height:41px;background:linear-gradient(var(--purple-light),var(--purple-dark));border-radius:3px}
.nav a{position:absolute;top:13px;color:var(--white);font-size:14px;text-decoration:none;font-weight:500}
.search{position:absolute;left:762px;top:7px;width:168px;height:27px;background:var(--white);border-radius:4px}
.search svg{position:absolute;right:4px;top:3px}

.hero{left:130px;top:197px;width:940px;height:358px;border:2px solid #eee;background:linear-gradient(100deg,#9a9a9a,#d6d4d0 35%,#c8c6c2 60%,#e4e2de);}
.hero-caption{position:absolute;left:0;top:169px;width:503px;height:95px;background:rgba(255,255,255,.72)}
.hero-title{position:absolute;left:31px;top:0;font-size:37px;color:var(--purple);white-space:nowrap}
.hero-sub{position:absolute;left:31px;top:40px;font-size:20px;line-height:26px;color:var(--ink)}
.hero-btn{position:absolute;left:31px;top:277px;width:182px;height:44px;background:#474747;border-radius:3px;color:var(--white);font-size:17px;text-align:center;line-height:44px;letter-spacing:.5px}
.dots{position:absolute;left:839px;top:330px;display:flex;gap:7px}
.dots i{width:14px;height:14px;border-radius:50%;background:#9a9a9a}
.dots i:first-child{background:var(--orange)}

.services{left:130px;top:568px;width:940px;height:197px;background:var(--orange-band);border-radius:3px}
.card{position:absolute;top:24px;width:168px;height:150px;background:linear-gradient(#fff,#e6e6e6);border:1px solid #ddd;text-align:center}
.card .icon{position:absolute;left:50px;top:18px;width:68px;height:68px;border-radius:50%;background:radial-gradient(circle at 40% 35%,#8a45b5,var(--purple-dark));border:3px solid var(--orange)}
.card .icon svg{position:absolute;left:13px;top:13px}
.card .label{position:absolute;left:0;width:100%;font-size:18px;line-height:23px;color:var(--ink);letter-spacing:.3px}

.welcome-title{left:130px;top:781px;font-size:22px;color:var(--purple)}
.welcome-text{left:130px;top:813px;width:615px;font-size:13px;line-height:23px;color:var(--body)}
.welcome-text .lead{color:var(--purple)}
.read-more{left:130px;top:952px;font-size:12px;font-weight:500;color:var(--ink)}

.news{left:770px;top:783px;width:300px;height:182px;background:#f0f0f0;border-radius:4px}
.news-title{position:absolute;left:21px;top:11px;font-size:21px;color:var(--purple)}
.news-arrows{position:absolute;right:10px;top:15px}
.news-head{position:absolute;left:23px;top:43px;width:250px;font-size:14px;line-height:18px;color:var(--orange-text)}
.news-body{position:absolute;left:23px;top:80px;width:260px;font-size:13px;line-height:20px;color:var(--body)}
.news-more{position:absolute;right:24px;top:152px;font-size:12px;font-weight:500;color:var(--purple)}

.rule{left:130px;top:984px;width:940px;height:1px;background:#ddd}
.portfolio-title{left:130px;top:999px;font-size:22px;color:var(--purple)}
.portfolio-arrows{left:1026px;top:1000px}
.thumb{position:absolute;top:1039px;width:170px;height:100px;border:2px solid #fff;box-shadow:0 0 4px rgba(0,0,0,.25)}

.footer{left:0;top:1161px;width:1200px;height:176px;background:var(--footer)}
.footer .abs{color:var(--white)}
.f-blog{left:130px;top:16px;font-size:21px;color:var(--orange)!important}
.f-post{left:131px;top:53px;width:270px;font-size:13px;line-height:18px;font-weight:500}
.f-date{left:131px;top:106px;font-size:12px;font-style:italic;color:var(--orange)!important}
.f-all{left:288px;top:139px;font-size:12px;font-weight:500}
.f-div{position:absolute;top:25px;width:1px;height:132px;background:#777}
.f-head{font-size:15px;font-weight:500}
.f-links a{position:absolute;font-size:13px;color:var(--orange);text-decoration:none;white-space:nowrap}
.social a{padding-left:30px}
.social a::before{content:"";position:absolute;left:0;top:0;width:16px;height:16px;background:#dcdcdc;border-radius:2px}
.f-brand{left:940px;top:27px}
.f-brand .sq{position:absolute;left:47px;top:0;width:32px;height:32px;background:#cfcfcf;border-radius:2px}
.f-brand .nm{position:absolute;left:0;top:42px;font-size:22px;color:#e0e0e0;white-space:nowrap;letter-spacing:1px}
.f-copy{right:128px;top:114px;text-align:right;font-size:12px;line-height:23px;color:#e6e6e6!important}
.f-copy span{color:var(--orange)}
</style>
</head>
<body>
<div class="stage">
  <div class="top-band"></div>
  <div class="page"></div>

  <div class="abs brand">
    <div class="brand-mark"></div>
    <div class="brand-name">THE VANTAGE</div>
  </div>

  <div class="abs contact">
    <div>Call Us : <strong>404-555-0182</strong></div>
    <div>Email : <span class="mail">rhoda@thevantagecomm.com</span></div>
  </div>

  <nav class="abs nav">
    <a style="left:17px">Home</a>
    <a style="left:92px">About Us</a>
    <a style="left:189px">Services</a>
    <a style="left:285px">Portfolio</a>
    <a style="left:387px">Blog</a>
    <a style="left:464px">Latest News</a>
    <a style="left:588px">Contact Us</a>
    <div class="search">
      <svg width="24" height="22" viewBox="0 0 24 22"><circle cx="9" cy="9" r="6.5" fill="none" stroke="#333" stroke-width="2.5"/><line x1="14" y1="14" x2="21" y2="20" stroke="#333" stroke-width="3.5" stroke-linecap="round"/></svg>
    </div>
  </nav>

  <section class="abs hero" role="img" aria-label="Photo of a smiling business team in suits">
    <div class="hero-caption">
      <div class="hero-title">The Vantage Communications</div>
      <div class="hero-sub">An independent marketing communications<br>PR writing and consulting group...</div>
    </div>
    <div class="hero-btn">VIEW PORTFOLIO</div>
    <div class="dots"><i></i><i></i><i></i><i></i></div>
  </section>

  <section class="abs services">
    <div class="card" style="left:20px">
      <div class="icon"><svg width="36" height="36" viewBox="0 0 36 36"><path d="M24 4 L31 11 L17 27 L9 29 L11 21 Z" fill="#f0a000"/><circle cx="15" cy="21" r="2" fill="#5a2180"/></svg></div>
      <div class="label" style="top:108px">WRITING</div>
    </div>
    <div class="card" style="left:203px">
      <div class="icon"><svg width="36" height="36" viewBox="0 0 36 36"><circle cx="18" cy="18" r="15" fill="none" stroke="#f0a000" stroke-width="2"/><path d="M18 3 L21 18 L18 33 L15 18 Z M3 18 L18 15 L33 18 L18 21 Z" fill="#f0a000"/></svg></div>
      <div class="label" style="top:97px">MARKETING<br>STRATEGY</div>
    </div>
    <div class="card" style="left:387px">
      <div class="icon"><svg width="36" height="36" viewBox="0 0 36 36"><rect x="12" y="2" width="12" height="20" rx="6" fill="#f0a000"/><path d="M8 16 Q8 27 18 27 Q28 27 28 16" fill="none" stroke="#f0a000" stroke-width="2.5"/><line x1="18" y1="27" x2="18" y2="33" stroke="#f0a000" stroke-width="2.5"/><line x1="11" y1="34" x2="25" y2="34" stroke="#f0a000" stroke-width="2.5"/></svg></div>
      <div class="label" style="top:97px">PUBLIC<br>RELATIONS</div>
    </div>
    <div class="card" style="left:571px">
      <div class="icon"><svg width="36" height="36" viewBox="0 0 36 36"><path d="M18 2 C9 2 5 9 7 15 C8 19 12 21 12 25 L24 25 C24 21 28 19 29 15 C31 9 27 2 18 2 Z" fill="none" stroke="#f0a000" stroke-width="2.5"/><rect x="13" y="27" width="10" height="3" fill="#f0a000"/><rect x="14" y="31" width="8" height="3" fill="#f0a000"/></svg></div>
      <div class="label" style="top:98px;font-size:17px;line-height:21px">THOUGHT LEADER<br>DEVELOPMENT</div>
    </div>
    <div class="card" style="left:754px">
      <div class="icon"><svg width="36" height="36" viewBox="0 0 36 36"><circle cx="18" cy="9" r="7" fill="none" stroke="#f0a000" stroke-width="3"/><rect x="16.5" y="16" width="3" height="18" fill="#f0a000"/><rect x="19" y="25" width="5" height="3" fill="#f0a000"/><rect x="19" y="30" width="4" height="3" fill="#f0a000"/></svg></div>
      <div class="label" style="top:108px">TRAINING</div>
    </div>
  </section>

  <h2 class="abs welcome-title" style="font-weight:400">Welcome to Our Site</h2>
  <div class="abs welcome-text">
    <p>The Vantage is an independent marketing communications and public relations writing and consulting firm. Big words, simple idea: We develop marketing and PR plans that work. We write really good copy. We pitch, write and (brag, brag) place articles so you look good to the people you want to look good to...among other things.</p>
    <p class="lead">Go ahead, cruise our site. Then give us a call or fire off an email if there's anything we can do for you.</p>
  </div>
  <div class="abs read-more">READ MORE &gt;&gt;</div>

  <aside class="abs news">
    <div class="news-title">News</div>
    <svg class="news-arrows" width="34" height="16" viewBox="0 0 34 16"><path d="M8 2 L3 8 L8 14 M26 2 L31 8 L26 14" fill="none" stroke="#555" stroke-width="2"/></svg>
    <div class="news-head">The Vantage Communications Awarded NWBA Certification</div>
    <div class="news-body">Aliquam molestie, mi et imperdiet euismod, dui purus auctor tellus, et interdum lacus lectus et ante.</div>
    <div class="news-more">READ MORE</div>
  </aside>

  <div class="abs rule"></div>
  <h2 class="abs portfolio-title" style="font-weight:400">Our Portfolio</h2>
  <svg class="abs portfolio-arrows" width="46" height="22" viewBox="0 0 46 22"><path d="M11 2 L3 11 L11 20 M35 2 L43 11 L35 20" fill="none" stroke="#555" stroke-width="2.5"/></svg>
  <div class="thumb" style="left:130px;background:linear-gradient(135deg,#7a5a3a,#e8e4de 50%,#b08050)" role="img" aria-label="Hands signing a document"></div>
  <div class="thumb" style="left:322px;background:linear-gradient(135deg,#f2f2f2,#d8d8d8 60%,#c04040)" role="img" aria-label="Open printed brochure"></div>
  <div class="thumb" style="left:515px;background:linear-gradient(135deg,#1a2a5a,#2a6ac0 50%,#e0e8f0)" role="img" aria-label="Website layout sample"></div>
  <div class="thumb" style="left:707px;background:linear-gradient(135deg,#9aa8b8,#3a3a44 60%,#1a1a1a)" role="img" aria-label="Press conference microphones"></div>
  <div class="thumb" style="left:899px;background:linear-gradient(135deg,#6a2a2a,#c89a78 50%,#e8d8b8)" role="img" aria-label="Team meeting around a table"></div>

  <footer class="abs footer">
    <div class="abs f-blog">Blog Post</div>
    <div class="abs f-post">The Vantage Communications Awarded NWBA Certification...</div>
    <div class="abs f-date">Posted on 3 hrs ago</div>
    <div class="abs f-all">READ ALL POSTS</div>
    <div class="f-div" style="left:432px"></div>
    <div class="f-div" style="left:663px"></div>
    <div class="f-div" style="left:813px"></div>

    <div class="abs f-head" style="left:453px;top:23px">Quick Links</div>
    <div class="f-links">
      <a style="left:453px;top:51px">Home</a>
      <a style="left:453px;top:78px">About Us</a>
      <a style="left:453px;top:105px">Services</a>
      <a style="left:453px;top:132px">Portfolio</a>
      <a style="left:561px;top:51px">Blog</a>
      <a style="left:561px;top:78px">Latest News</a>
      <a style="left:561px;top:105px">Contact Us</a>
    </div>

    <div class="abs f-head" style="left:693px;top:23px">Quick Links</div>
    <div class="f-links social">
      <a style="left:693px;top:51px">Social Page</a>
      <a style="left:693px;top:78px">Microblog</a>
      <a style="left:693px;top:105px">Network</a>
      <a style="left:693px;top:132px">Video Channel</a>
    </div>

    <div class="abs f-brand">
      <div class="sq"></div>
      <div class="nm">THE VANTAGE</div>
    </div>
    <div class="abs f-copy">Copyright © 2013 <span>The Vantage Communications</span><br>All Rights Reserved.</div>
  </footer>
</div>
</body>
</html>
```